BRAVOK PRESSURE WASHING LLC

am starting a small pressure washing business in myrtle beach. I need a weebsite that will get people attention. I wanrto advertise our services . Main two : We specialize in roof cleaning , window cleaning . Other services are : residential and commercial, driveways & sidewalks, gutter cleaning, patio & deck cleaning, curb appeal, heavy equipment, mobile homes, car lots, fleets, store fronts, commercial buildings, grocery kart sanitizing, have a couple phrases saying. " Make your home shine" " Make your home look new again" I need a section showing our work in the past. Im going to send you some ,before and after pictures of our work. Also put the 100% satisfaction guaranteed ribbon somewhere on the website and give us a call for your free estiment 843 555 0176. Licensed and insured. Also need a page listing our services and a paragraph or two of the importance of that service. Maybe a section where customers can comment and give good reviews. I need it to have my logo and make it look modern and catch the eye . We founded in 2019 and use environmental amd pet friendly chemicals and top of the line pressure washing equipment. Thank you.l

```html
<!DOCTYPE html>
<html lang="en">
<head>
<meta charset="utf-8">
<title>Bravok Pressure Washing LLC</title>
<link href="https://fonts.googleapis.com/css2?family=Oswald:wght@600;700&family=Roboto:ital,wght@0,400;0,500;0,700;1,400&display=swap" rel="stylesheet">
<style>
:root{
  --blue:#1b8fd6;
  --navy:#0d3461;
  --ink:#1c1c1c;
  --text:#555;
  --muted:#888;
  --footer:#121212;
  --gold:#d9a92a;
  --white:#fff;
}
*{box-sizing:border-box;margin:0;padding:0}
html,body{width:1200px;height:5204px;overflow:hidden}
body{font-family:"Roboto",Arial,sans-serif;color:var(--ink);background:var(--white);position:relative}
section,header,footer{position:relative;width:1200px;overflow:hidden}
.abs{position:absolute}
.heading{font-family:"Oswald","Arial Narrow",sans-serif;font-weight:700;color:var(--ink);text-transform:uppercase;letter-spacing:.5px}
.section-title{font-size:40px;text-align:center;line-height:1}
.title-bar{width:60px;height:3px;background:var(--blue);margin:14px auto 0}
.intro{font-size:15px;line-height:26px;color:#444;text-align:center;width:700px;margin:18px auto 0}
.btn{display:inline-flex;align-items:center;justify-content:center;background:var(--blue);color:var(--white);font-weight:700;font-size:15px;text-transform:uppercase;letter-spacing:.3px;text-decoration:none}
.btn-outline{background:var(--white);color:var(--blue);border:2px solid var(--blue)}
.photo{position:absolute}

/* header */
.site-header{height:93px;background:var(--white)}
.brand{left:104px;top:16px;display:flex;align-items:center;gap:10px}
.brand-dot{width:40px;height:40px;border-radius:50%;background:var(--blue);flex:none}
.brand-name{font-weight:700;font-size:15px;line-height:18px;color:var(--navy);width:150px}
.nav-link{position:absolute;top:62px;font-size:14px;font-weight:500;color:var(--ink);text-decoration:none;text-transform:uppercase;white-space:nowrap}
.nav-link.active{color:var(--blue)}
.follow{left:748px;top:22px;font-size:10px;font-weight:500;color:#333}
.social-dot{width:28px;height:28px;border-radius:50%;position:absolute;top:14px}
.call{left:950px;top:8px;display:flex;align-items:center;gap:8px}
.call small{display:block;font-size:9px;font-weight:500;color:#333}
.call strong{display:block;font-size:17px;color:var(--blue);font-weight:500}

/* hero */
.hero{height:566px}
.hero-bg{inset:0;background:linear-gradient(100deg,#c9d5de 0%,#aebfcc 30%,#d8dde1 55%,#8e9aa5 100%)}
.hero-title{left:98px;top:170px;font-size:44px;line-height:46px;color:var(--navy);width:620px}
.hero-text{left:100px;top:272px;font-size:20px;line-height:31px;color:var(--white);width:620px}
.hero .btn{left:99px;top:356px;width:235px;height:51px}
.arrow-circle{width:34px;height:34px;border-radius:50%;border:1.5px solid rgba(255,255,255,.9);display:flex;align-items:center;justify-content:center}
.dots{left:558px;top:521px;display:flex;gap:8px}
.dots span{width:12px;height:12px;border-radius:50%;background:var(--white)}
.dots span.current{background:transparent;border:2px solid var(--white)}

/* services */
.services{height:872px;background:var(--white)}
.services .section-title{padding-top:124px}
.service-card{position:absolute;top:270px;width:240px;height:390px;background:var(--white);box-shadow:0 2px 10px rgba(0,0,0,.14);text-align:center}
.service-card .photo{left:0;top:0;width:240px;height:174px}
.service-icon{position:absolute;left:89px;top:142px;width:62px;height:62px;border-radius:50%;background:var(--blue);border:3px solid var(--white);display:flex;align-items:center;justify-content:center}
.service-card h3{position:absolute;top:214px;left:0;width:100%;font-size:16px;font-weight:500;text-transform:uppercase;line-height:24px;padding:0 20px}
.service-card p{position:absolute;top:252px;left:0;width:100%;font-size:13px;line-height:24px;color:var(--text);padding:0 24px}
.service-card .btn{position:absolute;left:40px;top:332px;width:160px;height:46px}
.side-arrow{top:446px}
.services .btn-outline{left:484px;top:702px;width:232px;height:47px}

/* cta */
.cta{height:321px;background:var(--navy)}
.cta-title{left:232px;top:62px;font-size:40px;color:var(--white)}
.cta-text{left:232px;top:130px;width:660px;font-size:22px;line-height:33px;color:var(--white)}
.cta .btn{left:232px;top:212px;width:233px;height:47px}
.badge{left:52px;top:90px;width:150px;height:150px;border-radius:50%;background:var(--gold)}
.washer{left:900px;top:-50px;width:300px;height:330px;background:radial-gradient(ellipse at 60% 55%,#c6252b 0%,#8b1d22 38%,#1e1e1e 62%,transparent 63%)}

/* welcome */
.welcome{height:621px;background:#f2f3f4}
.welcome-photo{left:0;top:0;width:720px;height:621px;background:linear-gradient(90deg,#4f5a3a 0%,#7c7a55 30%,#b9a98a 55%,rgba(242,243,244,0) 100%)}
.welcome-kicker{left:634px;top:117px;font-size:26px}
.welcome-title{left:634px;top:155px;font-size:36px;width:540px}
.welcome .title-bar{position:absolute;left:634px;top:215px;margin:0}
.welcome-text{left:634px;top:240px;width:470px;font-size:15px;line-height:27px;color:#444}
.welcome .btn{left:634px;top:450px;width:160px;height:48px}

/* projects */
.projects{height:828px;background:var(--white)}
.projects .section-title{padding-top:122px}
.project{position:absolute;top:268px;width:322px;text-align:center}
.project .photo{position:relative;width:322px;height:267px;display:flex}
.project .half{flex:1}
.project .divider{width:3px;background:#e0c51f}
.project h3{margin-top:26px;font-size:20px;font-weight:500;text-transform:uppercase;letter-spacing:.5px}
.project p{margin-top:10px;font-size:14px;color:var(--muted)}
.projects .btn{left:465px;top:654px;width:270px;height:51px}

/* reviews */
.reviews{height:685px;background:linear-gradient(180deg,#143d6b 0%,#1a4674 40%,#12355f 100%)}
.reviews .section-title{padding-top:114px;color:var(--white)}
.reviews .intro{color:var(--white);width:640px}
.review-card{position:absolute;top:270px;width:317px;height:297px;background:var(--white);border-bottom:6px solid var(--blue);padding:28px 24px}
.source-dot{position:absolute;right:24px;top:26px;width:28px;height:28px;border-radius:50%;border:3px solid #ccc}
.review-card blockquote{margin-top:20px;font-size:17px;font-style:italic;line-height:29px;color:#333;text-align:justify}
.review-card cite{display:block;margin-top:14px;font-style:normal;font-weight:700;font-size:17px}

/* blogs */
.blogs{height:775px;background:var(--white)}
.blogs .section-title{padding-top:124px}
.post{position:absolute;top:282px;width:300px;height:372px;background:var(--white);box-shadow:0 2px 10px rgba(0,0,0,.12);border-bottom:5px solid var(--navy)}
.post.featured{border-bottom-color:var(--blue)}
.post .photo{position:relative;width:300px;height:186px}
.post time{display:block;margin:20px 0 0 16px;font-size:12px;color:var(--blue)}
.post h3{margin:8px 16px 0;font-size:16px;font-weight:500;line-height:26px}
.post p{margin:10px 16px 0;font-size:13px;line-height:25px;color:#666}

/* footer */
.site-footer{height:443px;background:var(--footer);color:var(--white)}
.footer-brand{left:99px;top:78px;display:flex;align-items:center;gap:10px}
.footer-brand .brand-name{color:var(--white);font-size:18px;line-height:22px;width:170px}
.license{left:110px;top:186px;font-size:13px}
.footer-social{left:110px;top:222px;display:flex;gap:8px}
.footer-social span{width:30px;height:30px;border-radius:50%;border:2px solid var(--white);background:#2a2a2a}
.footer-col h4{font-size:15px;font-weight:500;text-transform:uppercase}
.footer-col ul{list-style:none;margin-top:16px}
.quick li{font-size:14px;line-height:29px}
.contact li{font-size:14px;line-height:22px;display:flex;gap:12px;margin-bottom:20px}
.contact .ic{flex:none;width:22px;height:22px;border-radius:50%;background:#e5e5e5;display:flex;align-items:center;justify-content:center}
.subscribe p{margin-top:18px;font-size:14px;line-height:28px;width:280px}
.subscribe form{margin-top:16px;display:flex;width:268px;height:46px}
.subscribe .field{flex:1;background:var(--white);color:#999;font-size:13px;display:flex;align-items:center;padding-left:14px;gap:8px}
.subscribe .send{width:50px;background:var(--blue);display:flex;align-items:center;justify-content:center}
.footer-rule{left:99px;top:382px;width:1002px;height:1px;background:#444}
.copyright{left:110px;top:396px;font-size:13px}
.legal{left:820px;top:396px;font-size:13px}
</style>
</head>
<body>

<header class="site-header">
  <div class="abs brand"><span class="brand-dot"></span><span class="brand-name">BRAVOK PRESSURE WASHING</span></div>
  <nav>
    <a class="nav-link active" href="#" style="left:408px">Home</a>
    <a class="nav-link" href="#" style="left:512px">About</a>
    <a class="nav-link" href="#" style="left:616px">Services</a>
    <a class="nav-link" href="#" style="left:748px">Projects</a>
    <a class="nav-link" href="#" style="left:881px">Reviews</a>
    <a class="nav-link" href="#" style="left:1008px">Contact Us</a>
  </nav>
  <div class="abs follow">FOLLOW US</div>
  <span class="social-dot" style="left:822px;background:#3b5fb0"></span>
  <span class="social-dot" style="left:858px;background:#1f9be6"></span>
  <span class="social-dot" style="left:894px;background:#222"></span>
  <div class="abs call">
    <svg width="26" height="26" viewBox="0 0 24 24" fill="none" stroke="#1b8fd6" stroke-width="1.8"><path d="M5 3h4l2 5-3 2a12 12 0 0 0 6 6l2-3 5 2v4a2 2 0 0 1-2 2A18 18 0 0 1 3 5a2 2 0 0 1 2-2z"/></svg>
    <div><small>CALL US</small><strong>843-555-0176</strong></div>
  </div>
</header>

<section class="hero">
  <div class="abs hero-bg" role="img" aria-label="Freshly cleaned house roof and sparkling windows"></div>
  <h1 class="abs heading hero-title">Make your home shine. Roof &amp; window cleaning.</h1>
  <p class="abs hero-text">Make your home look new again with pet friendly, eco safe products and top of the line equipment</p>
  <a class="abs btn" href="#">Get a free estimate</a>
  <div class="abs arrow-circle" style="left:24px;top:360px"><svg width="12" height="12" viewBox="0 0 12 12" fill="none" stroke="#fff" stroke-width="1.6"><path d="M8 1 3 6l5 5"/></svg></div>
  <div class="abs arrow-circle" style="left:1120px;top:360px"><svg width="12" height="12" viewBox="0 0 12 12" fill="none" stroke="#fff" stroke-width="1.6"><path d="m4 1 5 5-5 5"/></svg></div>
  <div class="abs dots"><span></span><span></span><span class="current"></span><span></span></div>
</section>

<section class="services">
  <h2 class="heading section-title">Our Services</h2>
  <div class="title-bar"></div>
  <p class="intro">We specialize in roof cleaning and window cleaning, plus driveways, patios, decks, gutters, store fronts, fleets and commercial buildings across Myrtle Beach.</p>

  <svg class="abs side-arrow" style="left:54px" width="16" height="30" viewBox="0 0 16 30" fill="none" stroke="#333" stroke-width="1.6"><path d="M14 1 2 15l12 14"/></svg>
  <svg class="abs side-arrow" style="left:1130px" width="16" height="30" viewBox="0 0 16 30" fill="none" stroke="#333" stroke-width="1.6"><path d="m2 1 12 14L2 29"/></svg>

  <article class="service-card" style="left:99px">
    <div class="photo" role="img" aria-label="Worker soft washing a shingle roof" style="background:linear-gradient(160deg,#7c8a97,#3f4a55)"></div>
    <div class="service-icon"><svg width="28" height="28" viewBox="0 0 24 24" fill="none" stroke="#fff" stroke-width="1.6"><path d="M2 12 12 4l10 8M5 10v10h14V10"/><path d="M10 20v-5h4v5"/></svg></div>
    <h3>Roof Cleaning</h3>
    <p>Remove black streaks, moss and algae safely to protect your roof</p>
    <a class="btn" href="#">Learn more</a>
  </article>
  <article class="service-card" style="left:353px">
    <div class="photo" role="img" aria-label="Clean glass windows on a house front" style="background:linear-gradient(180deg,#a8c4dc,#5f88ad 60%,#3f5f7e)"></div>
    <div class="service-icon"><svg width="28" height="28" viewBox="0 0 24 24" fill="none" stroke="#fff" stroke-width="1.6"><rect x="4" y="3" width="16" height="18"/><path d="M12 3v18M4 12h16"/></svg></div>
    <h3>Window Cleaning</h3>
    <p>Streak free glass inside and out for a home that truly shines</p>
    <a class="btn" href="#">Learn more</a>
  </article>
  <article class="service-card" style="left:607px">
    <div class="photo" role="img" aria-label="Worker clearing a roof gutter" style="background:linear-gradient(180deg,#7fa6c4,#3f6b3c 60%,#5a5a5a)"></div>
    <div class="service-icon"><svg width="28" height="28" viewBox="0 0 24 24" fill="none" stroke="#fff" stroke-width="1.6"><path d="M3 6h18l-2 5H5zM12 11v8M9 19h6"/></svg></div>
    <h3>Gutter Cleaning</h3>
    <p>Clear leaves and debris so water flows away from your home</p>
    <a class="btn" href="#">Learn more</a>
  </article>
  <article class="service-card" style="left:861px">
    <div class="photo" role="img" aria-label="Concrete driveway being pressure washed" style="background:linear-gradient(160deg,#b3b0a8,#7c7a73 60%,#5c5a55)"></div>
    <div class="service-icon"><svg width="28" height="28" viewBox="0 0 24 24" fill="none" stroke="#fff" stroke-width="1.6"><path d="M8 3 4 21M16 3l4 18M12 5v3M12 11v3M12 17v3"/></svg></div>
    <h3>Driveways &amp; Sidewalks</h3>
    <p>Lift oil, dirt and stains to boost your curb appeal</p>
    <a class="btn" href="#">Learn more</a>
  </article>

  <a class="abs btn btn-outline" href="#">View more services</a>
</section>

<section class="cta">
  <div class="abs badge" role="img" aria-label="Satisfaction guarantee badge"></div>
  <h2 class="abs heading cta-title">Call us for free quote</h2>
  <p class="abs cta-text">10% off your next visit with referrals. call now for your free Estimate 843-555-0176 Licensed : 2071943 , insured : 306412</p>
  <a class="abs btn" href="#">Get a free estimate</a>
  <div class="abs washer" role="img" aria-label="Red gas pressure washer machine with spray wand"></div>
</section>

<section class="welcome">
  <div class="abs welcome-photo" role="img" aria-label="Man pressure washing a wooden fence in sunlight"></div>
  <p class="abs heading welcome-kicker">Welcome To</p>
  <h2 class="abs heading welcome-title">Bravok Pressure Washing LLC</h2>
  <div class="title-bar"></div>
  <p class="abs welcome-text">Founded in 2019, we are a Myrtle Beach pressure washing team that makes your home look new again. We use environmentally and pet friendly cleaning products with top of the line equipment. From roofs and windows to driveways, decks and store fronts, we treat every property with care. Licensed and insured, with a 100% satisfaction guarantee on every job we do for you.</p>
  <a class="abs btn" href="#">Learn more</a>
</section>

<section class="projects">
  <h2 class="heading section-title">Recent Projects</h2>
  <div class="title-bar"></div>
  <p class="intro">Lorem ipsum dolor sit amet, consectetur adipiscing elit, sed do eiusmod tempor incididunt ut labore et dolore magna aliqua. Quis ipsum suspendisse ultrices gravida.</p>

  <article class="project" style="left:99px">
    <div class="photo" role="img" aria-label="Driveway before and after pressure washing">
      <div class="half" style="background:linear-gradient(180deg,#9fb0a8,#6d6f69 45%,#8a8780)"></div><div class="divider"></div><div class="half" style="background:linear-gradient(180deg,#a7b8ad,#5f7051 40%,#bdbbb4)"></div>
    </div>
    <h3>Debris Removal</h3><p>Gutter Cleaning in Cheshire,CT</p>
  </article>
  <article class="project" style="left:438px">
    <div class="photo" role="img" aria-label="Paved yard before and after pressure washing">
      <div class="half" style="background:linear-gradient(180deg,#6d6a5e,#4d4b44 45%,#7a766c)"></div><div class="divider"></div><div class="half" style="background:linear-gradient(180deg,#6f6c60,#55534a 40%,#9d9a92)"></div>
    </div>
    <h3>Debris Removal</h3><p>Gutter Cleaning in Cheshire,CT</p>
  </article>
  <article class="project" style="left:777px">
    <div class="photo" role="img" aria-label="House front and lawn before and after cleaning">
      <div class="half" style="background:linear-gradient(180deg,#b9c3c8,#6a5e51 40%,#6c7a4c)"></div><div class="divider"></div><div class="half" style="background:linear-gradient(180deg,#b9c3c8,#7a6b5a 40%,#5f7440)"></div>
    </div>
    <h3>Debris Removal</h3><p>Gutter Cleaning in Cheshire,CT</p>
  </article>

  <a class="abs btn" href="#">See all recent projects</a>
</section>

<section class="reviews" role="img" aria-label="Faded house rooftops behind a navy overlay">
  <h2 class="heading section-title">Customer Reviews</h2>
  <div class="title-bar"></div>
  <p class="intro">Lorem ipsum dolor sit amet, consectetur adipiscing elit, sed do eiusmod tempor incididunt ut labore et dolore magna aliqua. Quis ipsum suspendisse ultrices gravida.</p>

  <svg width="0" height="0" style="position:absolute"><defs><path id="star" d="M8 0l2.4 5 5.4.6-4 3.7 1.1 5.4L8 12 3.1 14.7l1.1-5.4-4-3.7L5.6 5z"/></defs></svg>

  <article class="review-card" style="left:87px">
    <svg width="90" height="16" viewBox="0 0 90 16" fill="#e8a317"><use href="#star"/><use href="#star" x="18"/><use href="#star" x="36"/><use href="#star" x="54"/><use href="#star" x="72"/></svg>
    <span class="source-dot"></span>
    <blockquote>Lorem ictetur adipiscing elit, sed do eiusmod tempor incididunt ut labore et dolore magna aliqua. Quis ipsum suspendisse ultrices gravida.</blockquote>
    <cite>- Dana Whitfield</cite>
  </article>
  <article class="review-card" style="left:437px">
    <svg width="90" height="16" viewBox="0 0 90 16" fill="#e8a317"><use href="#star"/><use href="#star" x="18"/><use href="#star" x="36"/><use href="#star" x="54"/><use href="#star" x="72"/></svg>
    <span class="source-dot"></span>
    <blockquote>Lorem ictetur adipiscing elit, sed do eiusmod tempor incididunt ut labore et dolore magna aliqua. Quis ipsum suspendisse ultrices gravida.</blockquote>
    <cite>- Dana Whitfield</cite>
  </article>
  <article class="review-card" style="left:787px">
    <svg width="90" height="16" viewBox="0 0 90 16" fill="#e8a317"><use href="#star"/><use href="#star" x="18"/><use href="#star" x="36"/><use href="#star" x="54"/><use href="#star" x="72"/></svg>
    <span class="source-dot"></span>
    <blockquote>Lorem ictetur adipiscing elit, sed do eiusmod tempor incididunt ut labore et dolore magna aliqua. Quis ipsum suspendisse ultrices gravida.</blockquote>
    <cite>- Dana Whitfield</cite>
  </article>
</section>

<section class="blogs">
  <h2 class="heading section-title">Recent Blogs</h2>
  <div class="title-bar"></div>
  <p class="intro">Lorem ipsum dolor sit amet, consectetur adipiscing elit, sed do eiusmod tempor incididunt ut labore et dolore magna aliqua. Quis ipsum suspendisse ultrices gravida.</p>

  <article class="post" style="left:109px">
    <div class="photo" role="img" aria-label="Brick storefront with white posts" style="background:linear-gradient(180deg,#7a3a2e,#4b2a24 50%,#c9c6c0)"></div>
    <time>08 OCT 2020</time>
    <h3>Lorem ipsum dolsit amconsectetur adipiscing elit, sed do</h3>
    <p>Lorem ipsum dolor sit amet, consectetur adipiscing elit, sed do eiusmod ....</p>
  </article>
  <article class="post featured" style="left:445px">
    <div class="photo" role="img" aria-label="Worker pressure washing a wooden deck" style="background:linear-gradient(150deg,#5e8a4a,#b98b52 50%,#8a6a45)"></div>
    <time>08 AUG 2020</time>
    <h3>Lorem ipsum dolsit amconsectetur adipiscing elit, sed do</h3>
    <p>Lorem ipsum dolor sit amet, consectetur adipiscing elit, sed do eiusmod ....</p>
  </article>
  <article class="post" style="left:781px">
    <div class="photo" role="img" aria-label="Worker pressure washing a driveway in front of a house" style="background:linear-gradient(180deg,#7b6b5e,#8e8a80 50%,#b5b2aa)"></div>
    <time>08 AUG 2020</time>
    <h3>Lorem ipsum dolsit amconsectetur adipiscing elit, sed do</h3>
    <p>Lorem ipsum dolor sit amet, consectetur adipiscing elit, sed do eiusmod ....</p>
  </article>
</section>

<footer class="site-footer">
  <div class="abs footer-brand"><span class="brand-dot"></span><span class="brand-name">BRAVOK PRESSURE WASHING</span></div>
  <p class="abs license">CSLB LICENSE # 2071943</p>
  <div class="abs footer-social"><span></span><span></span><span></span><span></span></div>

  <div class="abs footer-col quick" style="left:340px;top:84px">
    <h4>Quick Links</h4>
    <ul><li>Home</li><li>About</li><li>Services</li><li>Projects</li><li>Reviews</li><li>Contact Us</li></ul>
  </div>

  <div class="abs footer-col contact" style="left:508px;top:84px">
    <h4>Contact Us</h4>
    <ul>
      <li><span class="ic"><svg width="10" height="12" viewBox="0 0 10 12" fill="#222"><path d="M5 0a4 4 0 0 1 4 4c0 3-4 8-4 8S1 7 1 4a4 4 0 0 1 4-4z"/></svg></span><span>412 Harbor View Lane<br>Myrtle Beach, SC 29577</span></li>
      <li><span class="ic"><svg width="11" height="11" viewBox="0 0 24 24" fill="#222"><path d="M5 3h4l2 5-3 2a12 12 0 0 0 6 6l2-3 5 2v4a2 2 0 0 1-2 2A18 18 0 0 1 3 5a2 2 0 0 1 2-2z"/></svg></span><span>843-555-0176</span></li>
      <li><span class="ic"><svg width="11" height="9" viewBox="0 0 12 9" fill="none" stroke="#222" stroke-width="1.3"><rect x=".6" y=".6" width="10.8" height="7.8"/><path d="m1 1 5 4 5-4"/></svg></span><span>info@bravokpressurewashing.com</span></li>
      <li><span class="ic"><svg width="11" height="11" viewBox="0 0 12 12" fill="none" stroke="#222" stroke-width="1.3"><circle cx="6" cy="6" r="5"/><path d="M6 3v3l2 1.5"/></svg></span><span>monday – friday:10:00 – 16:00<br>saturday:12:00 – 15:00 sunday &amp;<br>holidays:09:00 – 12:00</span></li>
    </ul>
  </div>

  <div class="abs footer-col subscribe" style="left:829px;top:84px">
    <h4>Subscribe to our blog</h4>
    <p>Sign up today to get resources on how to attract and retain more customers!</p>
    <form>
      <div class="field"><svg width="12" height="9" viewBox="0 0 12 9" fill="none" stroke="#999" stroke-width="1.2"><rect x=".6" y=".6" width="10.8" height="7.8"/><path d="m1 1 5 4 5-4"/></svg>Email Address</div>
      <div class="send"><svg width="18" height="18" viewBox="0 0 24 24" fill="#fff"><path d="M2 11 22 3l-6 18-4-7z"/></svg></div>
    </form>
  </div>

  <div class="abs footer-rule"></div>
  <p class="abs copyright">Copyright © 2020. Bravok Pressure Washing Llc  All Rights Reserved</p>
  <p class="abs legal">Terms and Conditions &nbsp;| &nbsp;Privacy Policy</p>
</footer>

</body>
</html>
```